Sex trafficking Survivor Newsletter

I would like an email newsletter template- mail chimp ready. The first will be a letter to update supporters on all the new changes. see attached.
Another template will have more blocks- for monthly use. I am envisioning a beautiful banner- possibly incorporating logo and photo(black woman holding sun); a main section (cover story, success story, teaching moments); news section; possibly three boxes at the bottom (spotlight- encouraging story of advocate or survivor, Get involved, Events)
I will be using mailchimp.
Let me know if you need more details.

```html
<!DOCTYPE html>
<html lang="en">
<head>
<meta charset="utf-8">
<title>Risen Anew – Supporter Update</title>
<link rel="stylesheet" href="https://fonts.googleapis.com/css2?family=Gelasio:ital,wght@0,400;0,700;1,700&display=swap">
<style>
  :root {
    --page-grey: #c9c9c9;
    --panel-white: #ffffff;
    --ink: #222222;
    --ink-soft: #6d6d6d;
    --brand-blue: #1f4f8c;
    --sky: #2aa8df;
    --quote-blue: #5cc6f2;
    --leaf: #8cc63f;
    --magenta: #d4145a;
    --royal: #1a72b9;
    --sun-1: #f6c779;
    --sun-2: #e58a3a;
    --sun-3: #6b3a25;
  }
  * { box-sizing: border-box; margin: 0; padding: 0; }
  html, body { width: 704px; height: 1200px; overflow: hidden; }
  body {
    position: relative;
    background: var(--page-grey);
    font-family: "Gelasio", Georgia, serif;
    color: var(--ink);
  }
  .masthead {
    position: absolute; left: 0; top: 0; width: 704px; height: 80px;
    background: var(--panel-white);
  }
  .brand {
    position: absolute; left: 28px; top: 16px;
    display: flex; align-items: center; gap: 10px;
  }
  .brand-dot { width: 30px; height: 30px; border-radius: 50%; background: var(--sky); }
  .brand-name {
    font-size: 26px; font-weight: 400; color: var(--brand-blue);
    letter-spacing: 0.5px;
  }
  .hero {
    position: absolute; left: 0; top: 80px; width: 704px; height: 311px;
    background:
      radial-gradient(ellipse at 55% 40%, #fbe3b2 0%, rgba(251,227,178,0) 45%),
      linear-gradient(100deg, var(--sun-3) 0%, var(--sun-2) 30%, var(--sun-1) 55%, var(--sun-2) 78%, var(--sun-3) 100%);
  }
  .hero-quote {
    position: absolute; left: 304px; top: 120px; width: 238px;
    font-size: 19px; line-height: 24px; font-style: italic; font-weight: 700;
    color: var(--quote-blue); text-align: center;
  }
  .panel {
    position: absolute; background: var(--panel-white);
    font-size: 10px; line-height: 13.5px; font-weight: 700;
  }
  .tag {
    position: absolute; height: 28px; color: #fff;
    font-size: 15px; line-height: 28px; padding-left: 30px; font-weight: 400;
  }
  .letter { left: 25px; top: 411px; width: 399px; height: 154px; padding: 14px 20px; }
  .salutation { font-size: 17px; font-weight: 400; margin-bottom: 12px; }
  .rename { left: 441px; top: 411px; width: 236px; height: 154px; }
  .rename-tag { left: 429px; top: 417px; width: 214px; background: var(--sky); padding-left: 16px; }
  .rename-old {
    position: absolute; left: 14px; top: 52px;
    font-size: 19px; font-weight: 400; color: var(--ink);
  }
  .rename-now { position: absolute; left: 158px; top: 58px; font-size: 13px; font-weight: 400; }
  .rename-new {
    position: absolute; left: 14px; top: 102px;
    display: flex; align-items: center; gap: 8px;
  }
  .rename-new .brand-dot { width: 26px; height: 26px; }
  .rename-new .brand-name { font-size: 20px; }
  .new-name { left: 25px; top: 584px; width: 652px; height: 120px; padding: 51px 28px 0 28px; }
  .new-name-tag { left: 13px; top: 597px; width: 219px; background: var(--leaf); }
  .opportunity { left: 25px; top: 724px; width: 648px; height: 176px; padding: 55px 28px 0 28px; }
  .opportunity-tag { left: 13px; top: 740px; width: 219px; background: var(--magenta); }
  .vision-title { color: var(--magenta); font-size: 12px; line-height: 15px; }
  .vision-line { color: var(--ink-soft); font-size: 12px; line-height: 15px; margin-bottom: 10px; }
  .director { left: 25px; top: 919px; width: 648px; height: 134px; padding: 52px 28px 0 28px; }
  .director-tag { left: 13px; top: 932px; width: 219px; background: var(--royal); }
  .closing {
    position: absolute; left: 25px; top: 1088px; width: 660px;
    font-size: 10px; line-height: 13.5px; font-weight: 700; color: #4a4a4a;
  }
  .closing p + p { margin-top: 10px; }
</style>
</head>
<body>
  <header class="masthead">
    <div class="brand">
      <span class="brand-dot"></span>
      <span class="brand-name">Risen Anew</span>
    </div>
  </header>

  <section class="hero" role="img" aria-label="Photo of two smiling women laughing together in warm golden sunlight">
    <p class="hero-quote">“Survivors of sexual exploitation live free, fulfilling their God-given purpose”</p>
  </section>

  <article class="panel letter">
    <p class="salutation">Dear Nora,</p>
    <p>I am writing to tell you of some exciting updates with Willow Wells. We have seen amazing transformation in the lives of sexually exploited women since 2011, and we couldn’t have done this without your support and partnership. Women have literally started new lives and escaped the horrors of their past abuse.</p>
  </article>

  <aside class="panel rename">
    <span class="rename-old">Willow Wells</span>
    <span class="rename-now">is now</span>
    <div class="rename-new">
      <span class="brand-dot"></span>
      <span class="brand-name">Risen Anew</span>
    </div>
  </aside>
  <h2 class="tag rename-tag">We changed our name</h2>

  <section class="panel new-name">
    <p>We officially changed our name to Risen Anew to emphasize the total transformation women experience and the sense of relief and freedom this brings. To be truly free and alive, a woman will experience change physically, emotionally, intellectually, and spiritually. Our name change highlights what women experience as we walk beside them. Many women say they were just existing in their former life. Now, they feel alive- for the first time.</p>
  </section>
  <h2 class="tag new-name-tag">New Name</h2>

  <section class="panel opportunity">
    <p class="vision-title">Our Vision</p>
    <p class="vision-line">Survivors of sexual exploitation live free, fulfilling their God-given purpose.</p>
    <p>In order to see our Vision become a reality, we need your help. As we journey forward walking closely with strong capable women, we would like to invite you to serve in a new capacity. We are launching a mentorship opportunity for female mentors to be paired with women who desperately need an advocate. Many survivors have never experienced a healthy supportive relationship, and do not know their God-given purpose. Your encouragement could be life changing!</p>
  </section>
  <h2 class="tag opportunity-tag">New Opportunity</h2>

  <section class="panel director">
    <p>While God has allowed me to be a part of such incredible transformation, I felt it was time to hire a new Executive Director to carry forward the vision and take the organization to the next level. I am pleased to announce the board and I have selected Lena Harlow, who comes to us with over 15 years of non-profit management experience. She has successfully initiated and developed initiatives that engaged thousands of laypeople in ministry to the poor. We are thrilled to have her leading the effort to accomplish our mission to “mobilize communities to encourage and equip survivors of sexual exploitation to build new lives.”</p>
  </section>
  <h2 class="tag director-tag">New Executive Director</h2>

  <footer class="closing">
    <p>It is a blessing that I can step away knowing we are in good hands and that God will continue to work through this ministry for His glory. I pray you will consider financially committing to the ministry and being a mentor so that we can continue to bless the survivors of sexual exploitation here in Dallas. Please visit us at www.risenanew.org</p>
    <p>Grace and Peace,<br>Dana Morrow</p>
  </footer>
</body>
</html>
```